Financial Services Sales Sheet

We need this sheet redesigned. Needs to feel very corporate/financial. open to imagery/icons/colors/etc. Copy is in the docx file to expedite work. PDF is what client has done inh-house and feels dated.

```html
<!DOCTYPE html>
<html lang="en">
<head>
<meta charset="utf-8">
<title>Master Servicing &amp; Portfolio Optimization — Harbor Ledger Partners</title>
<link rel="stylesheet" href="https://fonts.googleapis.com/css2?family=Montserrat:wght@600;700&family=Roboto+Condensed:ital,wght@0,400;0,700;1,700&family=Roboto:wght@400;500&display=swap">
<style>
  :root {
    --page: #ececed;
    --navy: #14315a;
    --navy-deep: #0f2442;
    --blue: #2c69a8;
    --blue-mid: #3b7bc0;
    --sky: #8fc1e3;
    --ink: #1a1a1a;
    --steel: #585a5d;
    --line: #b9bcc0;
    --card-bg: #eef0f2;
    --white: #ffffff;
  }
  * { margin: 0; padding: 0; box-sizing: border-box; }
  html, body { width: 1200px; height: 1200px; overflow: hidden; background: var(--page); }
  body { font-family: "Roboto", Arial, sans-serif; color: var(--ink); position: relative; }

  .sheet { position: absolute; left: 178px; top: 54px; width: 843px; height: 1091px; background: var(--white); overflow: hidden; }

  .masthead { position: absolute; left: 0; top: 0; width: 843px; height: 87px; }
  .masthead-visual { position: absolute; left: 0; top: 0; width: 520px; height: 87px;
    background: linear-gradient(120deg, #0d2446 0%, #1c4478 55%, #2a5e96 100%);
    clip-path: polygon(0 0, 470px 0, 520px 87px, 0 87px); }
  .brand { position: absolute; left: 548px; top: 24px; display: flex; align-items: center; gap: 12px; }
  .brand-mark { width: 30px; height: 30px; border-radius: 50%; background: var(--navy); }
  .brand-name { font-family: "Montserrat", sans-serif; font-weight: 700; font-size: 16px; line-height: 17px; color: var(--navy); letter-spacing: .3px; }

  .title-bar { position: absolute; left: 0; top: 87px; width: 843px; height: 60px;
    background: linear-gradient(180deg, #d4d6d9 0%, #b9bcc0 100%); }
  .title-bar h1 { font-family: "Montserrat", sans-serif; font-weight: 600; font-size: 29.5px; color: var(--navy-deep); position: absolute; left: 42px; top: 12px; letter-spacing: -.2px; white-space: nowrap; }

  .hero-visual { position: absolute; left: 422px; top: 147px; width: 421px; height: 255px;
    background: radial-gradient(circle at 55% 50%, #3d84c9 0%, #2b6aad 55%, #1f5792 100%); }

  .intro { position: absolute; left: 42px; top: 160px; width: 380px; }
  .intro h2 { font-family: "Roboto Condensed", sans-serif; font-weight: 700; font-size: 22.5px; line-height: 27px; color: var(--ink); padding-bottom: 9px; border-bottom: 1px solid var(--line); width: 320px; white-space: nowrap; }
  .intro p { font-size: 14px; line-height: 19.5px; margin-top: 12px; white-space: nowrap; }

  .pillars { position: absolute; left: 37px; top: 369px; display: flex; gap: 9px; }
  .pillar { width: 254px; height: 238px; border: 2px solid var(--line); border-radius: 6px; background: linear-gradient(180deg, #fff 0%, var(--card-bg) 100%); overflow: hidden; }
  .pillar-head { height: 64px; background: var(--navy); display: flex; align-items: center; gap: 12px; padding-left: 16px; color: var(--white); }
  .pillar-head svg { flex: 0 0 auto; }
  .pillar-head h3 { font-family: "Roboto Condensed", sans-serif; font-weight: 400; font-size: 19.5px; line-height: 21px; white-space: nowrap; }
  .pillar ul { list-style: none; padding: 10px 4px 0 24px; }
  .pillar li { font-family: "Roboto Condensed", sans-serif; font-size: 15px; line-height: 16.8px; position: relative; padding-left: 24px; white-space: nowrap; }
  .pillar li::before { content: ""; position: absolute; left: 0; top: 6px; width: 5px; height: 5px; background: var(--ink); }

  .snapshot-bar { position: absolute; left: 0; top: 629px; width: 843px; height: 32px; background: var(--steel); color: var(--white); font-family: "Roboto Condensed", sans-serif; font-size: 19px; line-height: 32px; padding-left: 35px; }

  .network-visual { position: absolute; left: 0; top: 770px; width: 843px; height: 255px;
    background: linear-gradient(180deg, #ffffff 0%, #e3eef8 45%, #cde1f2 100%); }

  .stats { position: absolute; left: 53px; top: 690px; display: flex; gap: 11px; }
  .stat { width: 174px; height: 77px; border: 2px solid var(--steel); border-radius: 4px; background: var(--white); text-align: center; padding-top: 7px; }
  .stat strong { display: block; font-family: "Roboto Condensed", sans-serif; font-weight: 400; font-size: 22.5px; line-height: 26px; }
  .stat span { display: block; font-family: "Roboto Condensed", sans-serif; font-size: 15px; line-height: 17.5px; white-space: nowrap; }

  .outcomes { position: absolute; left: 53px; top: 776px; display: flex; gap: 11px; }
  .outcome { width: 174px; text-align: center; }
  .outcome em { display: block; font-family: "Roboto Condensed", sans-serif; font-weight: 700; font-style: italic; font-size: 15.5px; white-space: nowrap; }
  .outcome svg { margin-top: 10px; }

  .platform { position: absolute; left: 191px; top: 889px; width: 462px; height: 110px; border: 2px solid #8a8d91; border-radius: 6px; background: var(--white); }
  .platform-label { position: absolute; left: 76px; top: -13px; width: 308px; height: 24px; background: var(--blue); border-radius: 4px; color: var(--white); font-family: "Roboto Condensed", sans-serif; font-size: 16px; line-height: 24px; text-align: center; white-space: nowrap; }
  .platform-items { display: flex; height: 100%; padding-top: 12px; }
  .platform-item { flex: 1; display: flex; align-items: center; justify-content: center; gap: 8px; font-family: "Roboto Condensed", sans-serif; font-size: 16px; line-height: 18.5px; text-align: center; white-space: nowrap; }
  .platform-item + .platform-item { border-left: 1px dashed var(--line); }

  .footer { position: absolute; left: 0; top: 1025px; width: 843px; height: 66px; display: flex; }
  .footer-tag { width: 491px; background: var(--steel); color: var(--white); font-family: "Roboto Condensed", sans-serif; font-size: 17px; line-height: 66px; padding-left: 33px; }
  .footer-web { flex: 1; background: var(--sky); color: var(--navy-deep); font-family: "Roboto Condensed", sans-serif; font-size: 17px; line-height: 66px; text-align: center; }
</style>
</head>
<body>
<main class="sheet">
  <header class="masthead">
    <div class="masthead-visual" role="img" aria-label="Dark blue digital world map with glowing data lines"></div>
    <div class="brand">
      <span class="brand-mark"></span>
      <span class="brand-name">HARBOR LEDGER<br>PARTNERS</span>
    </div>
  </header>

  <div class="title-bar"><h1>MASTER SERVICING &amp; PORTFOLIO OPTIMIZATION</h1></div>

  <div class="hero-visual" role="img" aria-label="Handshake in front of a protective shield surrounded by finance and compliance icons on a blue network background"></div>

  <section class="intro">
    <h2>End-to-End Post Default Management<br>Strategy, Recovery &amp; Compliance</h2>
    <p>HLP delivers master servicing solutions powered by<br>proprietary technology and automation. We centralize<br>back-office operations, optimize recovery<br>performance, and embed compliance controls across<br>the full post-default lifecycle, reducing client overhead<br>while increasing transparency and results.</p>
  </section>

  <section class="pillars">
    <article class="pillar">
      <div class="pillar-head">
        <svg width="48" height="40" viewBox="0 0 48 40" fill="none" stroke="#fff" stroke-width="2"><rect x="4" y="30" width="14" height="6"/><path d="M7 30l2-14h4l2 14M8 12h8M12 4v8"/><path d="M22 34l8-10 6 5 10-14"/><path d="M22 36h24"/></svg>
        <h3>Strategy &amp; Recovery<br>Optimization</h3>
      </div>
      <ul>
        <li>Recovery &amp; Liquidation<br>Optimization</li>
        <li>Settlement Campaigns</li>
        <li>Payer Base Development &amp;<br>Retention</li>
        <li>Penetration &amp; Conversion<br>Tracking</li>
        <li>Omni-Channel &amp; Champion<br>Challenger Collection Strategy</li>
      </ul>
    </article>
    <article class="pillar">
      <div class="pillar-head">
        <svg width="44" height="42" viewBox="0 0 44 42" fill="none" stroke="#fff" stroke-width="2"><path d="M22 3l16 6v11c0 10-7 16-16 19C13 36 6 30 6 20V9z"/><path d="M14 26l10-10M20 12l8 8M12 30h12"/></svg>
        <h3>Compliance &amp;<br>Risk Oversight</h3>
      </div>
      <ul>
        <li>Collection Agency Oversight</li>
        <li>Regulatory Compliance Audits<br>(FDCPA, FCRA, UDAAP)</li>
        <li>SOL Calculation &amp; Tracking</li>
        <li>Reg F Balance Reconciliations</li>
        <li>Bankruptcy, Military &amp; Deceased<br>Checks</li>
        <li>Complaint Management &amp;<br>Monitoring</li>
      </ul>
    </article>
    <article class="pillar">
      <div class="pillar-head">
        <svg width="46" height="42" viewBox="0 0 46 42" fill="none" stroke="#fff" stroke-width="2"><circle cx="15" cy="22" r="7"/><circle cx="15" cy="22" r="11" stroke-dasharray="4 3"/><ellipse cx="36" cy="26" rx="8" ry="3"/><path d="M28 26v10c0 2 16 2 16 0V26M28 31c0 2 16 2 16 0"/><circle cx="36" cy="8" r="4"/></svg>
        <h3>Operations &amp; Portfolio<br>Management</h3>
      </div>
      <ul>
        <li>Rigorous Placement &amp; Recall<br>Processing</li>
        <li>Daily Balance Calculations &amp;<br>Data Management</li>
        <li>Bank &amp; Inventory Reconciliation</li>
        <li>Portfolio Database Access</li>
        <li>Executive Reporting</li>
        <li>Bankruptcy Monitoring &amp; Support</li>
      </ul>
    </article>
  </section>

  <div class="snapshot-bar">PERFORMANCE SNAPSHOT</div>

  <div class="network-visual" role="img" aria-label="Light blue city skyline connected by a network of nodes and lines"></div>

  <section class="stats">
    <div class="stat"><strong>$155+ Million</strong><span>Portfolio Collections<br>Administered</span></div>
    <div class="stat"><strong>573,000+</strong><span>Defaulted Accounts<br>Managed</span></div>
    <div class="stat"><strong>3,700+</strong><span>Compliance Audits<br>Conducted</span></div>
    <div class="stat"><strong>21%</strong><span>3-Year Gross Collection<br>Curve</span></div>
  </section>

  <section class="outcomes">
    <div class="outcome"><em>Optimized Recoveries</em>
      <svg width="64" height="60" viewBox="0 0 64 60"><path d="M4 4v52h56" fill="none" stroke="#2c69a8" stroke-width="3"/><rect x="12" y="36" width="9" height="18" fill="#2c69a8"/><rect x="25" y="28" width="9" height="26" fill="#2c69a8"/><rect x="38" y="20" width="9" height="34" fill="#2c69a8"/><rect x="51" y="10" width="9" height="44" fill="#2c69a8"/><path d="M10 30l16-10 12 4 20-16" fill="none" stroke="#14315a" stroke-width="2.5"/></svg>
    </div>
    <div class="outcome"><em>Proven Scale</em>
      <svg width="60" height="60" viewBox="0 0 60 60" fill="#d9a52b" stroke="#a87a16" stroke-width="1.5"><ellipse cx="20" cy="50" rx="15" ry="5"/><ellipse cx="20" cy="43" rx="15" ry="5"/><ellipse cx="20" cy="36" rx="15" ry="5"/><ellipse cx="40" cy="30" rx="15" ry="5"/><ellipse cx="40" cy="23" rx="15" ry="5"/><ellipse cx="40" cy="16" rx="15" ry="5"/></svg>
    </div>
    <div class="outcome"><em>Embedded Compliance</em>
      <svg width="52" height="60" viewBox="0 0 52 60"><path d="M26 3l21 8v16c0 14-9 23-21 29C14 50 5 41 5 27V11z" fill="#1f5792"/><path d="M15 30l8 8 15-16" fill="none" stroke="#fff" stroke-width="5"/></svg>
    </div>
    <div class="outcome"><em>Measurable Outcomes</em>
      <svg width="64" height="60" viewBox="0 0 64 60"><rect x="6" y="38" width="8" height="18" fill="#2c69a8"/><rect x="18" y="30" width="8" height="26" fill="#2c69a8"/><rect x="30" y="34" width="8" height="22" fill="#2c69a8"/><rect x="42" y="24" width="8" height="32" fill="#2c69a8"/><path d="M4 34l14-12 12 8 24-22" fill="none" stroke="#2c69a8" stroke-width="4"/><path d="M46 6h12v12z" fill="#2c69a8"/></svg>
    </div>
  </section>

  <section class="platform">
    <div class="platform-label">PROPRIETARY TECHNOLOGY PLATFORM</div>
    <div class="platform-items">
      <div class="platform-item">
        <svg width="52" height="52" viewBox="0 0 56 56"><rect x="3" y="8" width="50" height="34" rx="3" fill="#14315a"/><rect x="20" y="44" width="16" height="4" fill="#14315a"/><rect x="14" y="48" width="28" height="3" fill="#14315a"/><path d="M28 12l11 4v8c0 7-5 11-11 14-6-3-11-7-11-14v-8z" fill="#3b7bc0"/><rect x="23" y="22" width="10" height="8" fill="#fff"/><path d="M25 22v-3a3 3 0 016 0v3" fill="none" stroke="#fff" stroke-width="2"/></svg>
        <span>Built-In<br>Compliance<br>Controls</span>
      </div>
      <div class="platform-item">
        <svg width="52" height="52" viewBox="0 0 56 56"><circle cx="18" cy="32" r="10" fill="none" stroke="#14315a" stroke-width="7" stroke-dasharray="5 3"/><circle cx="18" cy="32" r="5" fill="#14315a"/><circle cx="36" cy="14" r="7" fill="none" stroke="#3b7bc0" stroke-width="5" stroke-dasharray="4 2"/><path d="M32 32h14M32 42h14M46 32v10" stroke="#3b7bc0" stroke-width="2.5" fill="none"/><circle cx="48" cy="32" r="3" fill="#3b7bc0"/><circle cx="48" cy="42" r="3" fill="#3b7bc0"/></svg>
        <span>Centralized<br>Asset<br>Visibility</span>
      </div>
      <div class="platform-item">
        <svg width="52" height="52" viewBox="0 0 56 56" fill="none" stroke-width="5"><path d="M10 28a18 18 0 0131-12" stroke="#3b7bc0"/><path d="M46 28a18 18 0 01-31 12" stroke="#14315a"/><path d="M44 8v10H34" stroke="#3b7bc0" stroke-width="4"/><path d="M12 48V38h10" stroke="#14315a" stroke-width="4"/><circle cx="28" cy="28" r="6" stroke="#14315a" stroke-width="4"/></svg>
        <span>Automated<br>Workflow &amp;<br>Recovery<br>Execution</span>
      </div>
    </div>
  </section>

  <footer class="footer">
    <div class="footer-tag">Your Trusted Advisor.</div>
    <div class="footer-web">www.harborledger.com</div>
  </footer>
</main>
</body>
</html>
```